Stationary for Home Builder
Larkfield Dwellings Inc.
Project: Stationary for Home Builder
Stationary for Home Builder - Construction
Creative Brief
Modern
Gaston Villemure
Owner
Suite 310-7816 62 Avenue Edmonton, AB T5K 3M2
gaston@larkfielddwellings.ca
larkfielddwellings.ca
The blue colour used in the logo should be replicated and used within the stationary / business cards. Feel free to use additional complementary colours as well (including, but not limited to the grey colour used in the logo).. The intention is to have a modern feel but remain professional. The backside of the card can have designs but should allow some space to write notes.

```html
<!DOCTYPE html>
<html lang="en">
<head>
<meta charset="utf-8">
<title>Larkfield Dwellings Inc. – Business Cards</title>
<link href="https://fonts.googleapis.com/css2?family=Open+Sans:wght@400;600;700&display=swap" rel="stylesheet">
<style>
  :root {
    --page: #e6e9ed;
    --brand-blue: #2a85dc;
    --blue-light: #5eaaf0;
    --blue-dark: #1660c2;
    --grey-text: #3a3f47;
    --white: #ffffff;
    --silver-top: #f7f8fa;
    --silver-bottom: #d6dbe1;
  }
  * { box-sizing: border-box; margin: 0; padding: 0; }
  html, body { width: 1200px; height: 730px; overflow: hidden; }
  body {
    background: var(--page);
    font-family: "Open Sans", Arial, sans-serif;
    position: relative;
  }
  .card {
    position: absolute;
    width: 460px;
    height: 306px;
    border-radius: 20px;
    overflow: hidden;
    background: linear-gradient(180deg, var(--white) 0%, #eef1f4 100%);
    box-shadow: 0 6px 18px rgba(20, 40, 70, 0.22);
  }
  .card--frosted {
    background: rgba(255, 255, 255, 0.38);
    border: 1px solid rgba(255, 255, 255, 0.8);
    box-shadow: 0 6px 18px rgba(20, 40, 70, 0.12);
  }
  .card--front-solid   { left: 100px; top: 43px; }
  .card--front-frosted { left: 636px; top: 43px; }
  .card--back-solid    { left: 100px; top: 384px; }
  .card--back-frosted  { left: 636px; top: 384px; }

  .brand {
    position: absolute;
    left: 0; right: 0;
    top: 62px;
    display: flex;
    align-items: center;
    justify-content: center;
    gap: 10px;
  }
  .card--back-solid .brand,
  .card--back-frosted .brand { top: 72px; }
  .brand__mark {
    width: 14px; height: 14px;
    background: var(--brand-blue);
  }
  .brand__name {
    font-weight: 700;
    font-size: 26px;
    color: var(--brand-blue);
    letter-spacing: -0.3px;
  }
  .card--back-frosted .brand { opacity: 0.55; }

  .accent-line {
    position: absolute;
    left: 0; right: 0;
    top: 170px;
    height: 6px;
    background: linear-gradient(180deg, var(--blue-light), var(--blue-dark));
  }
  .name-band {
    position: absolute;
    left: 0; right: 0;
    top: 176px;
    height: 26px;
    background: linear-gradient(180deg, var(--silver-top), var(--silver-bottom));
    display: flex;
    align-items: center;
    justify-content: center;
    font-size: 11px;
    color: var(--grey-text);
  }
  .name-band__name { font-weight: 700; }
  .name-band__sep { margin: 0 6px; }

  .blue-band {
    position: absolute;
    left: 0; right: 0;
    background: linear-gradient(180deg, var(--blue-light) 0%, var(--brand-blue) 35%, var(--blue-dark) 100%);
    color: var(--white);
  }
  .card--front-solid .blue-band,
  .card--front-frosted .blue-band { top: 202px; height: 80px; padding: 16px 20px 0; }
  .card--front-frosted .blue-band { opacity: 0.9; }

  .contact-row {
    display: flex;
    align-items: center;
    gap: 14px;
    font-size: 9.5px;
    margin-bottom: 9px;
  }
  .contact-item { display: flex; align-items: center; gap: 4px; white-space: nowrap; }
  .contact-item svg { width: 12px; height: 12px; flex: none; }

  .card--back-solid .blue-band,
  .card--back-frosted .blue-band {
    top: 188px; height: 90px;
    display: flex; align-items: center; justify-content: center;
    font-size: 11px; letter-spacing: 3px;
    border-top: 2px solid #cfd6de;
  }
  .card--back-frosted .blue-band { opacity: 0.9; }
  .foot {
    position: absolute;
    left: 0; right: 0; bottom: 0;
    height: 24px;
    background: linear-gradient(180deg, var(--silver-bottom), var(--silver-top));
  }
  .card--front-solid .foot, .card--front-frosted .foot { background: var(--white); opacity: 0.85; }
</style>
</head>
<body>

<!-- Front, solid stock -->
<article class="card card--front-solid">
  <div class="brand"><span class="brand__mark"></span><span class="brand__name">Larkfield Dwellings Inc.</span></div>
  <div class="accent-line"></div>
  <div class="name-band"><span class="name-band__name">Gaston Villemure</span><span class="name-band__sep">|</span><span>Owner</span></div>
  <div class="blue-band">
    <div class="contact-row">
      <span class="contact-item"><svg viewBox="0 0 12 12"><circle cx="6" cy="6" r="6" fill="#fff"/><path d="M6 2.5a2 2 0 0 0-2 2c0 1.6 2 4.5 2 4.5s2-2.9 2-4.5a2 2 0 0 0-2-2z" fill="#1f6fcf"/></svg>Suite 310-7816 62 Avenue Edmonton, AB T5K 3M2</span>
      <span class="contact-item"><svg viewBox="0 0 12 12"><circle cx="6" cy="6" r="6" fill="#fff"/><path d="M3.5 7.5h5M6 3v3.5" stroke="#1f6fcf" stroke-width="1.2"/></svg>larkfielddwellings.ca</span>
    </div>
    <div class="contact-row">
      <span class="contact-item"><svg viewBox="0 0 12 12"><circle cx="6" cy="6" r="6" fill="#fff"/><path d="M4 3l1.2 1.5-.6 1c.5 1 1 1.5 1.9 1.9l1-.6L9 8l-1 1C5.5 8.8 3.2 6.5 3 4z" fill="#1f6fcf"/></svg>780.555.0142</span>
      <span class="contact-item"><svg viewBox="0 0 12 12"><circle cx="6" cy="6" r="6" fill="#fff"/><path d="M4 3l1.2 1.5-.6 1c.5 1 1 1.5 1.9 1.9l1-.6L9 8l-1 1C5.5 8.8 3.2 6.5 3 4z" fill="#1f6fcf"/></svg>780.555.0187</span>
      <span class="contact-item"><svg viewBox="0 0 12 12"><circle cx="6" cy="6" r="6" fill="#fff"/><rect x="3" y="4" width="6" height="4" fill="none" stroke="#1f6fcf"/><path d="M3 4l3 2.2L9 4" fill="none" stroke="#1f6fcf"/></svg>gaston@larkfielddwellings.ca</span>
    </div>
  </div>
  <div class="foot"></div>
</article>

<!-- Front, frosted stock -->
<article class="card card--frosted card--front-frosted">
  <div class="brand"><span class="brand__mark"></span><span class="brand__name">Larkfield Dwellings Inc.</span></div>
  <div class="accent-line"></div>
  <div class="name-band"><span class="name-band__name">Gaston Villemure</span><span class="name-band__sep">|</span><span>Owner</span></div>
  <div class="blue-band">
    <div class="contact-row">
      <span class="contact-item"><svg viewBox="0 0 12 12"><circle cx="6" cy="6" r="6" fill="#fff"/><path d="M6 2.5a2 2 0 0 0-2 2c0 1.6 2 4.5 2 4.5s2-2.9 2-4.5a2 2 0 0 0-2-2z" fill="#1f6fcf"/></svg>Suite 310-7816 62 Avenue Edmonton, AB T5K 3M2</span>
      <span class="contact-item"><svg viewBox="0 0 12 12"><circle cx="6" cy="6" r="6" fill="#fff"/><path d="M3.5 7.5h5M6 3v3.5" stroke="#1f6fcf" stroke-width="1.2"/></svg>larkfielddwellings.ca</span>
    </div>
    <div class="contact-row">
      <span class="contact-item"><svg viewBox="0 0 12 12"><circle cx="6" cy="6" r="6" fill="#fff"/><path d="M4 3l1.2 1.5-.6 1c.5 1 1 1.5 1.9 1.9l1-.6L9 8l-1 1C5.5 8.8 3.2 6.5 3 4z" fill="#1f6fcf"/></svg>780.555.0142</span>
      <span class="contact-item"><svg viewBox="0 0 12 12"><circle cx="6" cy="6" r="6" fill="#fff"/><path d="M4 3l1.2 1.5-.6 1c.5 1 1 1.5 1.9 1.9l1-.6L9 8l-1 1C5.5 8.8 3.2 6.5 3 4z" fill="#1f6fcf"/></svg>780.555.0187</span>
      <span class="contact-item"><svg viewBox="0 0 12 12"><circle cx="6" cy="6" r="6" fill="#fff"/><rect x="3" y="4" width="6" height="4" fill="none" stroke="#1f6fcf"/><path d="M3 4l3 2.2L9 4" fill="none" stroke="#1f6fcf"/></svg>gaston@larkfielddwellings.ca</span>
    </div>
  </div>
</article>

<!-- Back, solid stock -->
<article class="card card--back-solid">
  <div class="brand"><span class="brand__mark"></span><span class="brand__name">Larkfield Dwellings Inc.</span></div>
  <div class="blue-band">www.larkfielddwellings.ca</div>
  <div class="foot"></div>
</article>

<!-- Back, frosted stock -->
<article class="card card--frosted card--back-frosted">
  <div class="brand"><span class="brand__mark"></span><span class="brand__name">Larkfield Dwellings Inc.</span></div>
  <div class="blue-band">www.larkfielddwellings.ca</div>
</article>

</body>
</html>
```